Bref créative
QDRL Stationary
Professional
Delvonte Ashby
CEO
4815 Marigold Ln
Brookvale, TX 70000
dashby@qdrlinc.example
www.QDRLInc.example
My company Logo should be placed on the back of the card.

```html
<!DOCTYPE html>
<html lang="en">
<head>
<meta charset="utf-8">
<title>QDRL Business Card</title>
<link rel="stylesheet" href="https://fonts.googleapis.com/css2?family=Montserrat:wght@400;600;800&display=swap">
<style>
  :root {
    --backdrop: #5b5d60;
    --card-top: #ffffff;
    --card-bottom: #f4f5f4;
    --card-edge: #e6e8e6;
    --ink: #1b1d22;
    --ink-soft: #4a4c50;
    --green: #2e8d3b;
    --green-dark: #1f6b2a;
    --rule: #c9cbcc;
  }
  * { box-sizing: border-box; margin: 0; padding: 0; }
  html, body {
    width: 1200px;
    height: 787px;
    overflow: hidden;
    background: var(--backdrop);
    font-family: "Montserrat", sans-serif;
  }
  .canvas {
    position: relative;
    width: 1200px;
    height: 787px;
  }
  .card {
    position: absolute;
    width: 605px;
    height: 341px;
    background: linear-gradient(180deg, var(--card-top) 0%, var(--card-bottom) 100%);
    border-radius: 14px;
    overflow: hidden;
  }
  .card--front { left: 60px; top: 36px; }
  .card--back { left: 535px; top: 410px; }

  .front__band {
    position: absolute;
    left: 0; right: 0; bottom: 0;
    height: 22px;
    background: linear-gradient(180deg, var(--green) 0%, var(--green-dark) 100%);
    border-top: 3px solid var(--card-edge);
  }
  .brand {
    position: absolute;
    color: var(--ink);
    font-weight: 800;
    letter-spacing: 1px;
    line-height: 1;
  }
  .front__brand { left: 48px; top: 206px; font-size: 56px; }
  .front__divider {
    position: absolute;
    left: 300px; top: 46px;
    width: 1px; height: 240px;
    background: var(--rule);
  }
  .contact {
    position: absolute;
    left: 352px; top: 56px;
    color: var(--ink-soft);
  }
  .contact__name {
    font-size: 23px;
    font-weight: 600;
    color: var(--ink);
    line-height: 1.2;
  }
  .contact__role {
    font-size: 15px;
    line-height: 1.2;
    margin-bottom: 38px;
  }
  .contact__lines {
    list-style: none;
    font-size: 15px;
    line-height: 19.5px;
  }
  .contact__web {
    font-size: 15px;
    margin-top: 20px;
  }
  .back__brand { right: 44px; bottom: 26px; font-size: 50px; }
</style>
</head>
<body>
  <main class="canvas">
    <section class="card card--front" aria-label="Card front">
      <div class="brand front__brand">QDRL</div>
      <div class="front__divider"></div>
      <div class="contact">
        <p class="contact__name">Delvonte Ashby</p>
        <p class="contact__role">CEO</p>
        <ul class="contact__lines">
          <li>4815 Marigold Ln</li>
          <li>Brookvale, TX 70000</li>
          <li>T:&nbsp; 800-555-0147</li>
          <li>C:&nbsp; 254-555-0193</li>
          <li>F:&nbsp; 800-555-0147</li>
          <li>E:&nbsp; dashby@qdrlinc.example</li>
        </ul>
        <p class="contact__web">www.QDRLInc.example</p>
      </div>
      <div class="front__band"></div>
    </section>

    <section class="card card--back" aria-label="Card back">
      <div class="brand back__brand">QDRL</div>
    </section>
  </main>
</body>
</html>
```